Change logo on company documents

I want to change the logo on all company documents and change them company name that is written in certain places in the text.

Target Market(s)

Construction/Residential Home Remodeling

Colors

Designer to choose colors to be used in the design.

```html
<!DOCTYPE html>
<html lang="en">
<head>
<meta charset="utf-8">
<title>Certificate of Completion — Corvell Builders</title>
<link href="https://fonts.googleapis.com/css2?family=Montserrat:wght@700&family=Open+Sans:wght@400;700&display=swap" rel="stylesheet">
<style>
  :root {
    --backdrop: #c4c4c4;
    --paper: #ffffff;
    --ink: #1f2430;
    --ink-soft: #3a3f4a;
    --rule: #2b303a;
    --accent: #d9531e;
    --mark-faint: rgba(60, 70, 90, 0.05);
  }
  * { box-sizing: border-box; margin: 0; padding: 0; }
  html, body {
    width: 1200px; height: 909px; overflow: hidden;
    background: var(--backdrop);
    font-family: "Open Sans", Arial, sans-serif;
    color: var(--ink);
  }
  .certificate {
    position: absolute; left: 270px; top: 27px;
    width: 660px; height: 855px;
    background: var(--paper);
  }
  .certificate__frame {
    position: absolute; inset: 26px;
    border: 1px solid var(--rule);
  }
  .certificate__watermark {
    position: absolute; left: 150px; top: 300px;
    width: 360px; height: 360px;
  }
  .letterhead {
    position: absolute; left: 58px; right: 58px; top: 54px;
    display: flex; justify-content: space-between; align-items: flex-start;
  }
  .brand {
    display: flex; align-items: center; gap: 12px; margin-top: 36px;
  }
  .brand__dot {
    width: 30px; height: 30px; border-radius: 50%; background: var(--accent);
  }
  .brand__name {
    font-family: "Montserrat", Arial, sans-serif; font-weight: 700;
    font-size: 24px; line-height: 1; letter-spacing: 0.5px;
    color: var(--ink); text-transform: uppercase;
  }
  .contact {
    font-size: 8.5px; line-height: 1.45; text-align: right;
    text-transform: uppercase; letter-spacing: 0.6px; color: var(--ink-soft);
  }
  .certificate__title {
    position: absolute; left: 0; right: 0; top: 178px;
    text-align: center;
    font-family: "Montserrat", Arial, sans-serif; font-weight: 700;
    font-size: 21px; letter-spacing: 2.4px; color: var(--ink);
  }
  .field {
    position: absolute;
    border-top: 1px solid var(--rule);
    padding-top: 3px;
    font-size: 9px; color: var(--ink-soft);
  }
  .field--homeowner { left: 80px; top: 292px; width: 230px; }
  .field--completion { left: 400px; top: 258px; width: 180px; }
  .statement {
    position: absolute; left: 92px; right: 70px; top: 330px;
    font-size: 10.5px; line-height: 1.6; color: var(--ink);
  }
  .statement p + p { margin-top: 6px; }
  .blank {
    display: inline-block; width: 120px; border-bottom: 1px solid var(--rule);
    vertical-align: baseline;
  }
  .blank--wide { width: 165px; }
  .field--client { left: 92px; top: 560px; width: 200px; }
  .field--client-date { left: 92px; top: 612px; width: 200px; }
  .field--company { left: 370px; top: 560px; width: 200px; }
  .field--company-date { left: 370px; top: 612px; width: 200px; }
</style>
</head>
<body>
  <main class="certificate">
    <div class="certificate__frame"></div>
    <svg class="certificate__watermark" viewBox="0 0 360 360" aria-hidden="true">
      <circle cx="180" cy="180" r="170" fill="none" stroke="var(--mark-faint)" stroke-width="10"/>
    </svg>

    <header class="letterhead">
      <div class="brand">
        <span class="brand__dot"></span>
        <span class="brand__name">Corvell Builders</span>
      </div>
      <address class="contact" style="font-style: normal;">
        One Harbor Plaza<br>
        Suite 400 #118<br>
        Ridgeport, LA 70990<br>
        P: 555.014.2290<br>
        F: 555.014.7731
      </address>
    </header>

    <h1 class="certificate__title">CERTIFICATE OF COMPLETION</h1>

    <div class="field field--homeowner">Homeowner</div>
    <div class="field field--completion">Completion Date</div>

    <section class="statement">
      <p>I/We hereby certify that all necessary repairs as outlined in the contract between Corvell Roofing and
        <span class="blank"></span> located at <span class="blank blank--wide"></span>
        have been completed in a satisfactory manner and all liens will be waived upon final payment for labor and materials.</p>
      <p>All contractors, subcontractors and suppliers who have provided labor or materials in connection with the repairs to the property have been paid in full or will be paid from the final invoice proceeds.</p>
    </section>

    <div class="field field--client">Client</div>
    <div class="field field--client-date">Date</div>
    <div class="field field--company">Corvell Builders, LLC</div>
    <div class="field field--company-date">Date</div>
  </main>
</body>
</html>
```